Quote Cards for Social Media RV

I would like to put these quotes over one of the pictures attached; One Quote per picture, and I want the quote to be bold or easy to read as well. I provided a few reference graphics that I really like as examples below. In very small letters at the bottom add @RVCarloweDaily

All of the pictures are attached; you can pick any photo and add one quote to it; but no stock photography

Target Market(s)

women trying to lose weight

Requirements
Must have
• quotes and pictures attached
Should not have
• no stock photography

```html
<!DOCTYPE html>
<html lang="en">
<head>
<meta charset="utf-8">
<title>Quote Card – Overnight Remedy</title>
<link href="https://fonts.googleapis.com/css2?family=Work+Sans:wght@400;500;800&display=swap" rel="stylesheet">
<style>
  :root {
    --magenta: #c7339b;
    --navy: #2b2767;
    --white: #ffffff;
    --photo-warm: #c98f86;
    --photo-cream: #ece4e6;
    --photo-dark: #2f2428;
    --wand-pink: #eab8de;
  }
  html, body {
    margin: 0;
    padding: 0;
    width: 1198px;
    height: 1200px;
    overflow: hidden;
  }
  .quote-card {
    position: relative;
    width: 1198px;
    height: 1200px;
    background: var(--magenta);
    font-family: "Work Sans", sans-serif;
    overflow: hidden;
  }
  .text-panel {
    position: absolute;
    left: 43px;
    top: 0;
    width: 649px;
    height: 1200px;
    background: var(--white);
  }
  .headline-box {
    position: absolute;
    left: 43px;
    top: 0;
    width: 649px;
    height: 553px;
    background: var(--navy);
    border-bottom-right-radius: 26px;
  }
  .headline {
    position: absolute;
    left: 81px;
    top: 172px;
    margin: 0;
    color: var(--white);
    font-size: 72px;
    line-height: 89px;
    font-weight: 400;
    white-space: nowrap;
  }
  .remedy-line {
    position: absolute;
    left: 81px;
    top: 611px;
    margin: 0;
    color: var(--magenta);
    font-size: 78px;
    line-height: 85px;
    font-weight: 400;
    white-space: nowrap;
  }
  .strong { font-weight: 800; }
  .remedy-line .big { font-size: 96px; }
  .handle {
    position: absolute;
    left: 821px;
    top: 62px;
    color: var(--white);
    font-size: 34px;
    font-weight: 500;
  }
  .portrait {
    position: absolute;
    left: 705px;
    top: 310px;
    width: 470px;
    height: 890px;
    border-radius: 235px 235px 0 0;
    background: linear-gradient(180deg, var(--photo-dark) 0%, var(--photo-warm) 28%, var(--photo-cream) 52%, var(--photo-warm) 70%, var(--photo-dark) 82%, var(--photo-dark) 100%);
  }
  .wand {
    position: absolute;
    left: 455px;
    top: 985px;
    width: 180px;
    height: 150px;
    border-radius: 50%;
    background: radial-gradient(circle, var(--wand-pink) 0%, rgba(234, 184, 222, 0) 70%);
  }
</style>
</head>
<body>
  <main class="quote-card">
    <div class="text-panel"></div>
    <div class="headline-box"></div>
    <h1 class="headline">
      <span class="strong">WAKE UP</span><br>
      TOMORROW<br>
      WITH <span class="strong">A FLATTER</span><br>
      <span class="strong">BELLY</span>- YES,
    </h1>
    <p class="remedy-line">
      THIS<br>
      OVERNIGHT<br>
      <span class="strong big">REMEDY</span><br>
      WORKS LIKE<br>
      <span class="strong big">MAGIC!</span>
    </p>
    <div class="wand" role="img" aria-label="Small sparkling magic wand illustration"></div>
    <div class="portrait" role="img" aria-label="Photo of a smiling woman in a white cropped sweater pointing upward"></div>
    <div class="handle">@RVCarloweDaily</div>
  </main>
</body>
</html>
```